lakeview slab pumping "keep it flowing"

I want very easy to understand cards that say everything we offer.
i want the company name/logo, phone number and email on the front of card.
i want the card to stand out, it can be red with black lettering.
on the back of the card i want it to list everything that we can do like a list
the motto is JUST PUMP IT.
the can be in the lower right corner of the back of the card

Target Market(s)

concrete contractors

Industry/Entity Type

Concrete

Contact Information for Business Card

back of the card
Owner:Marco Feltz
Phone:503)418-6093
Email: LVSlabFlow@mailbox-example.com
address: 20918 ne marlow st Portland, OR 97236

Colors
ec1f27
000000
959595
5c5c5c
f04a50
ffffff
f37122

Requirements
Must have
• :we have years of experience in the world of concrete
• :our pumps can do up to 70 yards an hour
• :if you refer us to other contractors, will give you up to 10% off next pump job
• :don’t hesitate to call if you have any concrete related questions and to get a qoute
• Please put this on the front of the card, “just pump it” in the lower right corner

```html
<!DOCTYPE html>
<html lang="en">
<head>
<meta charset="utf-8">
<title>Lakeview Slab Pumping – Business Cards</title>
<link rel="stylesheet" href="https://fonts.googleapis.com/css2?family=Montserrat:wght@300;400;500;700;800&family=Open+Sans:wght@400;600&display=swap">
<style>
  :root {
    --red: #ec1f27;
    --red-soft: #f04a50;
    --black: #000000;
    --card-black: #111111;
    --grey: #959595;
    --grey-dark: #5c5c5c;
    --white: #ffffff;
    --stage: #2b2b2b;
    --line-soft: #e6e6e6;
  }
  * { margin: 0; padding: 0; box-sizing: border-box; }
  html, body {
    width: 1200px; height: 716px; overflow: hidden;
    background: var(--stage);
  }
  .stage {
    position: relative; width: 1200px; height: 716px;
    display: flex; align-items: center; justify-content: center; gap: 60px;
  }
  .card {
    position: relative; width: 520px; height: 297px;
    border-radius: 18px; overflow: hidden;
    box-shadow: 0 12px 30px rgba(0,0,0,.45);
  }

  /* Back card */
  .card--back {
    background: var(--card-black);
    display: flex; flex-direction: column; align-items: center; justify-content: center;
    color: var(--white);
  }
  .brand { text-align: center; }
  .brand__name {
    font-family: "Montserrat", sans-serif; font-weight: 800;
    color: var(--red); font-size: 50px; letter-spacing: 2px; line-height: 1;
  }
  .brand__sub {
    font-family: "Montserrat", sans-serif; font-weight: 400;
    color: #d8d8d8; font-size: 17px; letter-spacing: 5px; margin-top: 8px;
  }
  .brand__tagline {
    font-family: "Montserrat", sans-serif; font-weight: 300;
    color: var(--red-soft); font-size: 14px; letter-spacing: 1px;
    text-align: right; margin-top: 6px;
  }
  .brand__tagline strong { font-weight: 700; }
  .services {
    margin-top: 28px; font-family: "Open Sans", sans-serif;
    font-size: 14px; color: #dcdcdc; letter-spacing: .3px;
  }
  .services span.sep { margin: 0 8px; color: var(--grey); }

  /* Front card */
  .card--front { background: var(--white); }
  .front__decor {
    position: absolute; right: -40px; top: 40px;
    width: 240px; height: 240px; border-radius: 50%;
    background: #eeeeee;
  }
  .front__logo {
    position: absolute; left: 32px; top: 92px; text-align: left;
  }
  .front__logo .brand__name { font-size: 30px; letter-spacing: 1px; }
  .front__logo .brand__sub { color: var(--grey-dark); font-size: 10.5px; letter-spacing: 3.2px; margin-top: 5px; }
  .front__divider {
    position: absolute; left: 238px; top: 72px; width: 2px; height: 118px;
    background: var(--red);
  }
  .contact {
    position: absolute; left: 256px; top: 74px;
    font-family: "Montserrat", sans-serif; color: #1a1a1a;
  }
  .contact__name { font-size: 22px; letter-spacing: .5px; }
  .contact__name .first { font-weight: 300; }
  .contact__name .last { font-weight: 700; }
  .contact__role { color: var(--red); font-size: 13px; margin-top: 1px; }
  .contact__row {
    display: flex; align-items: center; gap: 8px;
    font-family: "Open Sans", sans-serif; font-size: 13px; margin-top: 9px;
  }
  .contact__row svg { width: 14px; height: 14px; flex: none; }
  .front__bands { position: absolute; left: 0; bottom: 0; width: 520px; height: 70px; }
  .band-text {
    position: absolute; font-family: "Open Sans", sans-serif; color: var(--white);
  }
  .band-text--pumps { left: 40px; bottom: 30px; font-size: 14px; }
  .band-text--refer { right: 38px; bottom: 14px; font-size: 15px; }
</style>
</head>
<body>
<main class="stage">

  <section class="card card--back">
    <div class="brand">
      <div class="brand__name">LAKEVIEW</div>
      <div class="brand__sub">SLAB PUMPING</div>
      <div class="brand__tagline">KEEP IT <strong>FLOWING</strong></div>
    </div>
    <div class="services">
      Our service 1<span class="sep">|</span>Our Service 2<span class="sep">|</span>Our Service 3
    </div>
  </section>

  <section class="card card--front">
    <div class="front__decor" aria-hidden="true"></div>

    <div class="front__logo brand">
      <div class="brand__name">LAKEVIEW</div>
      <div class="brand__sub">SLAB PUMPING</div>
    </div>

    <div class="front__divider"></div>

    <div class="contact">
      <div class="contact__name"><span class="first">MARCO</span> <span class="last">FELTZ</span></div>
      <div class="contact__role">Owner</div>
      <div class="contact__row">
        <svg viewBox="0 0 16 16" aria-hidden="true"><path fill="#ec1f27" d="M3 2h3l1.5 3.5-2 1.3a8 8 0 0 0 3.7 3.7l1.3-2L14 10v3a1 1 0 0 1-1 1A11 11 0 0 1 2 3a1 1 0 0 1 1-1z"/></svg>
        <span>(503)418-6093</span>
      </div>
      <div class="contact__row">
        <svg viewBox="0 0 16 16" aria-hidden="true"><rect x="1" y="3" width="14" height="10" rx="1" fill="#ec1f27"/><path d="M1.5 3.8 8 9l6.5-5.2" fill="none" stroke="#fff" stroke-width="1.3"/></svg>
        <span>LVSlabFlow@mailbox-example.com</span>
      </div>
    </div>

    <svg class="front__bands" viewBox="0 0 520 70" preserveAspectRatio="none" aria-hidden="true">
      <polygon points="0,10 330,10 300,70 0,70" fill="#000000"/>
      <polygon points="330,10 520,10 520,70 300,70" fill="#ffffff"/>
      <polygon points="318,32 520,32 520,70 300,70" fill="#ec1f27"/>
      <polygon points="325,10 340,10 318,32 303,32" fill="#ffffff"/>
    </svg>
    <div class="band-text band-text--pumps">Our pumps can do up to 70 yards an hour</div>
    <div class="band-text band-text--refer">Please refer us</div>
  </section>

</main>
</body>
</html>
```